Loan Application Project

We have a bank application form in pdf and we wish to use the content of the application to develop a loan application using our own brand and look / feel with the brand of a Partner.

The content of the application can be simply copied across. We assume that the process for doing this is easy when armed with the right pdf software.
Updates

Hi - I have now added both the second logo that needs incorporating and also gone through and made changes to the text on the actual application form so this project is now ready to "bring home".  Thanks Gordon

Target Market(s)

Samll Business Operators

Industry/Entity Type

Bank

Requirements
Must have
• Must remove all reference to Coastal Meridian Bank or CMB and replace with Tallow Credit Services Pty Ltd (Tallow). I'd be happy to go through the hard copy and scan a copy where I have hand written changes for the designer
Nice to have
• To be able to electronically complete the form would be great. Not sure how you do this but I know it can be done for pdf forms.

```html
<!DOCTYPE html>
<html lang="en">
<head>
<meta charset="utf-8">
<title>Entity 1 – Company/Business</title>
<link href="https://fonts.googleapis.com/css2?family=Fira+Sans:wght@400;600&display=swap" rel="stylesheet">
<style>
  :root {
    --ink: #231f20;
    --panel: #e3edeb;
    --field: #ffffff;
    --rule: #4a4a4a;
    --rule-soft: #9aa7a5;
    --bar: #000000;
  }
  * { box-sizing: border-box; margin: 0; padding: 0; }
  html, body { width: 849px; height: 1200px; overflow: hidden; background: #fff; }
  body { font-family: "Fira Sans", Arial, sans-serif; color: var(--ink); font-size: 10px; line-height: 12px; }
  .page { position: relative; width: 849px; height: 1200px; }
  .top-bar { position: absolute; left: 40px; top: 40px; width: 768px; height: 17px; background: var(--bar); }
  .panel { position: absolute; left: 40px; top: 68px; width: 768px; height: 1092px; background: var(--panel); border-top: 1px solid var(--rule); }
  .section-title { position: absolute; left: 50px; top: 70px; height: 16px; display: flex; align-items: center; gap: 7px; font-weight: 600; font-size: 12.5px; }
  .section-title::before { content: ""; width: 26px; height: 16px; background: var(--bar); }
  .section-rule { position: absolute; left: 50px; top: 86px; width: 749px; height: 1px; background: var(--rule-soft); }
  .lbl { position: absolute; white-space: nowrap; }
  .lbl b { font-weight: 600; }
  .heading { font-weight: 600; font-size: 10.5px; }
  .field { position: absolute; background: var(--field); border: 1px solid var(--rule-soft); border-bottom-color: var(--rule); border-left-color: var(--rule); }
  .field .in { position: absolute; top: 50%; transform: translateY(-50%); }
  .slash { position: absolute; top: 3px; }
  .tick { position: absolute; width: 11px; height: 11px; background: var(--field); border: 1px solid var(--rule); }
  .addr { position: absolute; background: var(--field); border: 1px solid var(--rule-soft); border-bottom-color: var(--rule); border-left-color: var(--rule); }
  .addr .line { position: absolute; left: 4px; right: 0; height: 1px; background: var(--rule); }
  .addr .foot { position: absolute; bottom: 0; left: 0; right: 0; height: 16px; background: var(--panel); }
  .addr .foot span { position: absolute; top: 3px; }
  .page-no { position: absolute; right: 49px; top: 1163px; font-size: 9px; }
</style>
</head>
<body>
<div class="page">
  <div class="top-bar"></div>
  <div class="panel"></div>
  <div class="section-title">Entity 1 – Company/Business</div>

  <!-- Left column -->
  <span class="tick" style="left:52px;top:103px"></span><span class="lbl" style="left:68px;top:104px">Borrower</span>
  <span class="tick" style="left:162px;top:103px"></span><span class="lbl" style="left:178px;top:104px">Guarantor</span>
  <span class="lbl" style="left:50px;top:124px">Full legal name of entity (e.g. Company, Business, Sole Trader)</span>
  <div class="field" style="left:50px;top:139px;width:365px;height:21px"></div>

  <span class="lbl heading" style="left:50px;top:166px">Business Structure <span style="font-weight:400">(Tick all that apply):</span></span>
  <span class="tick" style="left:52px;top:185px"></span><span class="lbl" style="left:68px;top:186px">Company (Proprietary/Public)</span>
  <span class="tick" style="left:220px;top:185px"></span><span class="lbl" style="left:236px;top:186px">Proprietorship (including sole traders)</span>
  <span class="tick" style="left:52px;top:205px"></span><span class="lbl" style="left:68px;top:206px">Partnership</span>
  <span class="tick" style="left:220px;top:205px"></span><span class="lbl" style="left:236px;top:206px">T/as a Business</span>
  <span class="tick" style="left:52px;top:224px"></span><span class="lbl" style="left:68px;top:225px">Other (i.e. Incorporated Assoc, Union, Self Managed Super Fund etc)</span>
  <div class="field" style="left:50px;top:241px;width:365px;height:20px"></div>

  <span class="lbl" style="left:50px;top:266px">A.C.N./A.R.B.N./A.B.N./Business Registration No.</span>
  <div class="field" style="left:50px;top:281px;width:365px;height:20px"></div>

  <span class="lbl" style="left:50px;top:306px">Date of incorporation<br>(if applicable)</span>
  <span class="lbl" style="left:193px;top:306px">Date Business Name Registered<br>(if applicable)</span>
  <div class="field" style="left:50px;top:333px;width:135px;height:20px"><span class="slash" style="left:52px">/</span><span class="slash" style="left:92px">/</span></div>
  <div class="field" style="left:193px;top:333px;width:133px;height:20px"><span class="slash" style="left:50px">/</span><span class="slash" style="left:91px">/</span></div>

  <span class="lbl" style="left:50px;top:359px">Business trading name (if applicable)</span>
  <div class="field" style="left:50px;top:374px;width:365px;height:20px"></div>
  <span class="lbl" style="left:50px;top:399px">Main business activity</span>
  <div class="field" style="left:50px;top:414px;width:365px;height:20px"></div>

  <span class="tick" style="left:52px;top:445px"></span><span class="lbl" style="left:68px;top:447px">Importer</span>
  <span class="tick" style="left:220px;top:445px"></span><span class="lbl" style="left:236px;top:447px">Exporter</span>
  <span class="lbl" style="left:50px;top:466px">Is this a Franchise?</span>
  <span class="tick" style="left:175px;top:464px"></span><span class="lbl" style="left:191px;top:466px">Yes</span>
  <span class="tick" style="left:236px;top:464px"></span><span class="lbl" style="left:252px;top:466px">No</span>
  <span class="lbl" style="left:50px;top:486px">Other Business Activity (if any)</span>
  <div class="field" style="left:50px;top:500px;width:365px;height:20px"></div>

  <span class="lbl" style="left:50px;top:532px">Date company/business commenced trading</span>
  <div class="field" style="left:281px;top:527px;width:134px;height:20px"><span class="slash" style="left:48px">/</span><span class="slash" style="left:90px">/</span></div>
  <span class="lbl" style="left:50px;top:558px">Total number of staff/employees</span>
  <div class="field" style="left:281px;top:553px;width:134px;height:20px"><span class="slash" style="left:48px">/</span><span class="slash" style="left:90px">/</span></div>

  <span class="lbl" style="left:50px;top:578px">Business address</span>
  <div class="addr" style="left:50px;top:593px;width:365px;height:58px">
    <div class="line" style="top:19px"></div><div class="line" style="top:39px"></div>
    <div class="foot" style="border-bottom:1px solid var(--rule)"><span style="left:13px">State</span><span style="left:113px">Postcode</span><span style="left:227px">Country</span></div>
  </div>
  <span class="lbl" style="left:50px;top:658px">Postal Address (if different from above)</span>
  <div class="addr" style="left:50px;top:673px;width:365px;height:62px">
    <div class="line" style="top:20px"></div><div class="line" style="top:42px"></div>
    <div class="foot" style="border-bottom:1px solid var(--rule)"><span style="left:13px">State</span><span style="left:113px">Postcode</span><span style="left:227px">Country</span></div>
  </div>

  <span class="lbl" style="left:50px;top:739px">Contact Name</span>
  <div class="field" style="left:50px;top:754px;width:365px;height:20px"></div>
  <span class="lbl" style="left:50px;top:780px">Contact telephone number</span>
  <span class="lbl" style="left:237px;top:780px">Contact facsimile number</span>
  <div class="field" style="left:50px;top:795px;width:179px;height:21px"><span class="in" style="left:15px">(&nbsp;&nbsp;&nbsp;&nbsp;)</span></div>
  <div class="field" style="left:237px;top:795px;width:178px;height:21px"><span class="in" style="left:14px">(&nbsp;&nbsp;&nbsp;&nbsp;)</span></div>
  <span class="lbl" style="left:50px;top:820px">Email address</span>
  <div class="field" style="left:50px;top:835px;width:365px;height:20px"></div>
  <span class="lbl" style="left:50px;top:860px">Website address</span>
  <div class="field" style="left:50px;top:875px;width:365px;height:20px"><span class="in" style="left:13px">http://</span></div>

  <span class="lbl" style="left:50px;top:909px">Is there are a Trust involved?</span>
  <span class="tick" style="left:223px;top:906px"></span><span class="lbl" style="left:239px;top:909px">Yes</span>
  <span class="tick" style="left:291px;top:906px"></span><span class="lbl" style="left:307px;top:909px">No</span>
  <span class="lbl" style="left:50px;top:928px">Name of Trust (if applicable)</span>
  <div class="field" style="left:50px;top:942px;width:365px;height:20px"></div>
  <span class="lbl" style="left:50px;top:968px">Type of Trust (if applicable), i.e. discretionary, family, unit trust</span>
  <div class="field" style="left:50px;top:983px;width:365px;height:20px"></div>
  <span class="lbl" style="left:50px;top:1009px">Date of Trust Deed</span>
  <span class="lbl" style="left:193px;top:1009px">Date/s of any variations</span>
  <div class="field" style="left:50px;top:1024px;width:135px;height:20px"><span class="slash" style="left:48px">/</span><span class="slash" style="left:90px">/</span></div>
  <div class="field" style="left:193px;top:1024px;width:133px;height:20px"><span class="slash" style="left:46px">/</span><span class="slash" style="left:88px">/</span></div>
  <span class="lbl" style="left:50px;top:1053px">How long has the company/business been<br>under the current ownership/management?</span>
  <div class="field" style="left:281px;top:1054px;width:134px;height:21px"><span class="in" style="right:10px">years</span></div>

  <!-- Right column -->
  <span class="lbl" style="left:434px;top:100px"><b>No. 1:</b> Full name of owner/partner/director</span>
  <div class="field" style="left:434px;top:115px;width:365px;height:20px"></div>
  <span class="lbl" style="left:434px;top:141px">Position/Title (e.g. Managing Director)</span>
  <span class="lbl" style="left:702px;top:141px">%Shareholding</span>
  <div class="field" style="left:434px;top:155px;width:260px;height:21px"></div>
  <div class="field" style="left:702px;top:155px;width:97px;height:21px"><span class="in" style="right:8px;font-weight:600">%</span></div>
  <span class="lbl" style="left:434px;top:181px">Residential address (not required if owner/partner/director is Entity 3 or 4)</span>
  <div class="addr" style="left:434px;top:196px;width:365px;height:56px">
    <div class="line" style="top:19px"></div><div class="line" style="top:39px"></div>
    <div class="foot" style="border-bottom:1px solid var(--rule)"><span style="left:13px">State</span><span style="left:113px">Postcode</span><span style="left:227px">Country</span></div>
  </div>

  <span class="lbl" style="left:434px;top:262px"><b>No. 2:</b> Full name of owner/partner/director</span>
  <div class="field" style="left:434px;top:276px;width:365px;height:20px"></div>
  <span class="lbl" style="left:434px;top:301px">Position/Title (e.g. Managing Director)</span>
  <span class="lbl" style="left:702px;top:301px">%Shareholding</span>
  <div class="field" style="left:434px;top:316px;width:260px;height:21px"></div>
  <div class="field" style="left:702px;top:316px;width:97px;height:21px"><span class="in" style="right:8px;font-weight:600">%</span></div>
  <span class="lbl" style="left:434px;top:342px">Residential address (not required if owner/partner/director is Entity 3 or 4)</span>
  <div class="addr" style="left:434px;top:356px;width:365px;height:57px">
    <div class="line" style="top:20px"></div><div class="line" style="top:40px"></div>
    <div class="foot" style="border-bottom:1px solid var(--rule)"><span style="left:13px">State</span><span style="left:113px">Postcode</span><span style="left:227px">Country</span></div>
  </div>

  <span class="lbl" style="left:434px;top:422px"><b>No. 3:</b> Full name of owner/partner/director</span>
  <div class="field" style="left:434px;top:437px;width:365px;height:20px"></div>
  <span class="lbl" style="left:434px;top:462px">Position/Title (e.g. Managing Director)</span>
  <span class="lbl" style="left:702px;top:462px">%Shareholding</span>
  <div class="field" style="left:434px;top:476px;width:260px;height:21px"></div>
  <div class="field" style="left:702px;top:476px;width:97px;height:21px"><span class="in" style="right:8px;font-weight:600">%</span></div>
  <span class="lbl" style="left:434px;top:502px">Residential address (not required if owner/partner/director is Entity 3 or 4)</span>
  <div class="addr" style="left:434px;top:517px;width:365px;height:57px">
    <div class="line" style="top:20px"></div><div class="line" style="top:40px"></div>
    <div class="foot" style="border-bottom:1px solid var(--rule)"><span style="left:13px">State</span><span style="left:113px">Postcode</span><span style="left:227px">Country</span></div>
  </div>

  <span class="lbl" style="left:434px;top:580px">Have owners/partners/directors/guarantors provided guarantees or security<br>to support any other borrowings at other financial institutions?</span>
  <span class="tick" style="left:437px;top:609px"></span><span class="lbl" style="left:453px;top:611px">No</span>
  <span class="tick" style="left:539px;top:609px"></span><span class="lbl" style="left:555px;top:611px">Yes (give details)</span>
  <div class="field" style="left:634px;top:607px;width:165px;height:21px"></div>
  <div class="field" style="left:434px;top:628px;width:365px;height:22px"></div>

  <span class="lbl heading" style="left:434px;top:658px">Main professional contacts <span style="font-weight:400">(Complete where applicable)</span></span>
  <span class="lbl" style="left:434px;top:677px">Accountant’s name</span>
  <div class="field" style="left:434px;top:691px;width:365px;height:21px"></div>
  <span class="lbl" style="left:434px;top:716px">Name of firm</span>
  <div class="field" style="left:434px;top:731px;width:365px;height:21px"></div>
  <span class="lbl" style="left:434px;top:764px">Telephone number</span>
  <div class="field" style="left:539px;top:757px;width:179px;height:21px"><span class="in" style="left:15px">(&nbsp;&nbsp;&nbsp;&nbsp;)</span></div>

  <span class="lbl" style="left:434px;top:783px">Solicitor’s name</span>
  <div class="field" style="left:434px;top:797px;width:365px;height:21px"></div>
  <span class="lbl" style="left:434px;top:822px">Name of firm</span>
  <div class="field" style="left:434px;top:837px;width:365px;height:21px"></div>
  <span class="lbl" style="left:434px;top:870px">Telephone number</span>
  <div class="field" style="left:539px;top:863px;width:179px;height:21px"><span class="in" style="left:15px">(&nbsp;&nbsp;&nbsp;&nbsp;)</span></div>

  <span class="lbl" style="left:434px;top:889px">Other professional contact name (Insurance Agent, Financial Adviser etc.)</span>
  <div class="field" style="left:434px;top:903px;width:365px;height:21px"></div>
  <span class="lbl" style="left:434px;top:929px">Name of firm</span>
  <div class="field" style="left:434px;top:943px;width:365px;height:21px"></div>
  <span class="lbl" style="left:434px;top:976px">Telephone number</span>
  <div class="field" style="left:539px;top:969px;width:179px;height:21px"><span class="in" style="left:15px">(&nbsp;&nbsp;&nbsp;&nbsp;)</span></div>

  <span class="lbl" style="left:434px;top:995px">Name of other key person 1 (Other than owner/partner/director) (if applicable)</span>
  <div class="field" style="left:434px;top:1009px;width:365px;height:21px"></div>
  <span class="lbl" style="left:434px;top:1037px">Title/Role</span>
  <span class="lbl" style="left:702px;top:1037px">Time in role</span>
  <div class="field" style="left:434px;top:1051px;width:260px;height:21px"></div>
  <div class="field" style="left:702px;top:1051px;width:97px;height:21px"></div>

  <span class="lbl" style="left:434px;top:1077px">Name of other key person 2 (Other than owner/partner/director) (if applicable)</span>
  <div class="field" style="left:434px;top:1091px;width:365px;height:21px"></div>
  <span class="lbl" style="left:434px;top:1119px">Title/Role</span>
  <span class="lbl" style="left:702px;top:1119px">Time in role</span>
  <div class="field" style="left:434px;top:1133px;width:260px;height:21px"></div>
  <div class="field" style="left:702px;top:1133px;width:97px;height:21px"></div>

  <span class="page-no">Page 2 of 14</span>
</div>
</body>
</html>
```